Kestrelwood Pathways Agency business cards

Australian company about to start offering its services. We recruit international students to come to study English, vocational education and postgraduate courses in Australia. We help them find the institution and select the right city they want to come to Australia. We are a young, online oriented and supportive agency. Our clients are between 18 and 35 years old, mainly University students, young professionals or people with work experience. We provide much more information that any other agency offer. We administrate a Facebook group with more than 11.000 members that daily ask questions about general information when coming to Australia, while they are here and even after they leave the country

Target Market(s)

International students from South America, Central America and Europe

Industry/Entity Type

Student

Contact Information for Business Card

Tomas Brevik
Managing Director
tomas@velmorin.com.au
www.velmorin.com.au
+61 491058263
Melbourne, Australia

Font styles to use
Serif
Sans Serif

Colors

Designer to choose colors to be used in the design.

Requirements
Must have
• Horizontal design
• Standard business card size and shape. If font uses green or yellow colours, they will have to match the ones from the logo
Nice to have
• UPDATE: Use the contents of the green image to design one of the card sides. Use our logo in the background of that side as watermark.
• Passport image, or immigration stamps. A picture of the Yarra River (from Melbourne) would be cool as well.
Should not have
• Non-standard business card size and shape
• Not black as the background colour of any sides as we are not a VIP agency or a hight class service. We are orientes to young people and they like colours, pictures, something attractive.
• Vertical design
• NO YELLOW or BLACK AS THE BACKGROUND COLOUR OF ANY SIDE OF THE BIZ CARD

```html
<!DOCTYPE html>
<html lang="en">
<head>
<meta charset="utf-8">
<title>Kestrelwood Pathways Agency – Business Cards</title>
<link rel="stylesheet" href="https://fonts.googleapis.com/css2?family=Open+Sans:wght@400;600;700&display=swap">
<style>
  :root {
    --backdrop: #e4e4e2;
    --gold: #d9b30d;
    --green-light: #15804a;
    --green: #0f6a3b;
    --green-deep: #0a5a31;
    --paper: #f4f4f2;
    --ink: #5e5e5e;
    --white: #ffffff;
  }
  * { box-sizing: border-box; margin: 0; padding: 0; }
  html, body {
    width: 1200px; height: 900px; overflow: hidden;
    background: var(--backdrop);
    font-family: "Open Sans", Arial, sans-serif;
  }
  .sheet {
    width: 1200px; height: 900px;
    display: flex; flex-direction: column;
    align-items: center; justify-content: center; gap: 40px;
  }
  .card {
    position: relative;
    width: 700px; height: 400px;
    overflow: hidden;
    box-shadow: 0 6px 18px rgba(0,0,0,.18);
  }

  /* Front */
  .card--front {
    background: linear-gradient(100deg, var(--green-light) 0%, var(--green) 50%, var(--green-deep) 100%);
  }
  .card--front::after {
    content: ""; position: absolute; left: 0; right: 0; bottom: 0;
    height: 8px; background: var(--gold);
  }
  .brand-name {
    font-family: "Open Sans", Arial, sans-serif;
    font-weight: 700;
    letter-spacing: 1px;
  }
  .card--front .brand-name {
    position: absolute; left: 0; right: 0; top: 118px;
    text-align: center; font-size: 66px; color: var(--white);
  }
  .tagline {
    position: absolute; left: 40px; right: 40px; top: 268px;
    display: flex; align-items: center; gap: 14px;
    color: var(--white); font-size: 15px; font-weight: 600;
  }
  .tagline::before, .tagline::after {
    content: ""; flex: 1; height: 1px; background: rgba(255,255,255,.8);
  }

  /* Back */
  .card--back { background: var(--paper); }
  .card__swoosh { position: absolute; inset: 0; }
  .person {
    position: absolute; right: 40px; top: 34px;
    text-align right; text-align: right; color: var(--white);
  }
  .person__name { font-size: 17px; font-weight: 700; text-transform: uppercase; letter-spacing: .3px; }
  .person__role { font-size: 16px; font-weight: 400; text-transform: uppercase; }
  .card--back .brand-name {
    position: absolute; left: 46px; top: 160px;
    font-size: 58px; color: var(--green);
  }
  .contact {
    position: absolute; left: 46px; bottom: 34px;
    color: var(--ink); font-size: 15px; line-height: 22px; list-style: none;
  }
  .contact__city { margin-bottom: 2px; }
  .contact li { display: flex; align-items: center; gap: 8px; }
  .contact svg { width: 13px; height: 13px; fill: var(--ink); flex: none; }
</style>
</head>
<body>
<main class="sheet">

  <section class="card card--front" aria-label="Card front">
    <div class="brand-name">Velmorin</div>
    <p class="tagline">Hacemos más por ti!</p>
  </section>

  <section class="card card--back" aria-label="Card back">
    <svg class="card__swoosh" viewBox="0 0 700 400" preserveAspectRatio="none" aria-hidden="true">
      <defs>
        <linearGradient id="greenBand" x1="0" y1="0" x2="1" y2="1">
          <stop offset="0" stop-color="#127443"/>
          <stop offset="1" stop-color="#0a5a31"/>
        </linearGradient>
      </defs>
      <path d="M150,128 C400,64 610,130 700,268 L700,250 C600,118 400,58 150,128 Z" fill="#d9b30d"/>
      <path d="M150,128 C400,58 600,118 700,250 L700,0 L300,0 Q240,92 150,128 Z" fill="url(#greenBand)"/>
    </svg>

    <div class="person">
      <div class="person__name">Tomas Brevik</div>
      <div class="person__role">Managing Director</div>
    </div>

    <div class="brand-name">Velmorin</div>

    <ul class="contact">
      <li class="contact__city">Melbourne, Australia</li>
      <li>
        <svg viewBox="0 0 16 16" aria-hidden="true"><path d="M3.6 1.2l2.3 2.6-1.2 1.6c.9 2 2.5 3.6 4.5 4.6l1.6-1.2 2.6 2.3-1.3 2.5C7 13.4 2.6 9 1.1 2.5z"/></svg>
        +61 491058263
      </li>
      <li>
        <svg viewBox="0 0 16 16" aria-hidden="true"><path d="M1 3h14v10H1z M2 4l6 5 6-5" stroke="#f4f4f2" stroke-width="1"/></svg>
        tomas@velmorin.com.au
      </li>
      <li>
        <svg viewBox="0 0 16 16" aria-hidden="true"><circle cx="8" cy="8" r="7"/><path d="M1 8h14M8 1c3 3 3 11 0 14M8 1c-3 3-3 11 0 14" stroke="#f4f4f2" stroke-width="1" fill="none"/></svg>
        www.velmorin.com.au
      </li>
    </ul>
  </section>

</main>
</body>
</html>
```